Bright Harbor need a basic Calendar design

Our customers like when we give them a calendar every year but we have undergone some changes in our branding and we seek a similar product to what we delivered, but with new logos and a fresh look. If you can incorporate some stock imagery or something that is fine (like the attached apples but not necessarily that image, thats fine). This is a basic corporate calendar,

See attached photos for what we are looking for. Essentially the same exact type of wall calendar with new logo and images. That is all.

Industry/Entity Type

Product

Font styles to use
Serif
Sans Serif

Colors
3277b5
0355a3
85abd2
ffffff

```html
<!DOCTYPE html>
<html lang="en">
<head>
<meta charset="utf-8">
<title>Bright Harbor 2015 Wall Calendar</title>
<link rel="stylesheet" href="https://fonts.googleapis.com/css2?family=Arimo:wght@400;700&family=Carlito:wght@700&family=Nunito:wght@800&display=swap">
<style>
  :root {
    --navy: #1c466f;
    --brand-blue: #3277b5;
    --deep-blue: #0355a3;
    --soft-blue: #85abd2;
    --white: #ffffff;
    --frame: #e4e5e8;
    --grid-line: #c8cbcf;
    --weekend: #eef0f3;
    --hole: #c4c6c9;
    --sub-grey: #7b7e82;
    --photo-light: #c9da78;
    --photo-mid: #a4c04a;
    --photo-dark: #7f9b32;
  }
  * { box-sizing: border-box; }
  html, body { margin: 0; padding: 0; overflow: hidden; background: var(--white); }
  .calendar {
    position: relative;
    width: 776px;
    height: 1200px;
    overflow: hidden;
    background: var(--white);
    font-family: "Arimo", Arial, sans-serif;
    color: var(--navy);
  }
  .hanger-hole {
    position: absolute;
    top: 15px;
    width: 13px;
    height: 13px;
    border-radius: 50%;
    background: var(--hole);
  }
  .year {
    position: absolute;
    left: 76px;
    top: 56px;
    margin: 0;
    font-weight: 700;
    font-size: 74px;
    line-height: 1;
    letter-spacing: 1px;
    color: var(--navy);
  }
  .brand {
    position: absolute;
    left: 508px;
    top: 64px;
    width: 200px;
  }
  .brand-line {
    display: flex;
    align-items: center;
    gap: 8px;
  }
  .brand-dot {
    width: 22px;
    height: 22px;
    border-radius: 50%;
    background: var(--brand-blue);
  }
  .brand-name {
    font-weight: 400;
    font-size: 25px;
    color: var(--brand-blue);
    line-height: 1;
  }
  .brand-division {
    margin-top: 6px;
    font-weight: 700;
    font-size: 10px;
    color: var(--sub-grey);
  }
  .hero-photo {
    position: absolute;
    left: 0;
    top: 127px;
    width: 776px;
    height: 204px;
    background: linear-gradient(180deg, var(--photo-light) 0%, var(--photo-mid) 50%, var(--photo-dark) 100%);
  }
  .tagline {
    position: absolute;
    left: 0;
    top: 282px;
    width: 776px;
    height: 49px;
    margin: 0;
    background: rgba(255, 255, 255, 0.6);
    font-family: "Carlito", Calibri, sans-serif;
    font-weight: 700;
    font-size: 23px;
    line-height: 49px;
    text-align: center;
    color: var(--navy);
  }
  .month {
    position: absolute;
    width: 306px;
    height: 264px;
    border: 4px solid var(--frame);
    border-radius: 13px;
    background: var(--white);
  }
  .month-name {
    margin: 0;
    height: 27px;
    border-radius: 9px 9px 0 0;
    background: var(--soft-blue);
    font-family: "Nunito", "Arial Rounded MT Bold", sans-serif;
    font-weight: 800;
    font-size: 21px;
    line-height: 27px;
    text-align: center;
    color: var(--navy);
  }
  .weekdays, .days {
    display: grid;
    grid-template-columns: repeat(7, 1fr);
    width: 286px;
    margin-left: 8px;
  }
  .weekdays {
    margin-top: 8px;
    height: 17px;
    font-weight: 700;
    font-size: 12px;
    text-align: center;
  }
  .days {
    margin-top: 4px;
    gap: 1px;
    padding: 1px;
    background: var(--grid-line);
  }
  .days span {
    height: 39px;
    padding: 4px 5px 0 0;
    background: var(--white);
    font-size: 11px;
    text-align: right;
  }
  .days span:nth-child(7n+1),
  .days span:nth-child(7n) { background: var(--weekend); }
  .footer-bar {
    position: absolute;
    left: 0;
    top: 1165px;
    width: 776px;
    height: 35px;
    display: flex;
    justify-content: space-between;
    align-items: center;
    padding: 0 36px 0 33px;
    background: var(--soft-blue);
    font-family: "Carlito", Calibri, sans-serif;
    font-weight: 700;
    font-size: 19px;
    color: var(--navy);
  }
</style>
</head>
<body>
<main class="calendar">
  <span class="hanger-hole" style="left:298px"></span>
  <span class="hanger-hole" style="left:440px"></span>

  <h1 class="year">2015</h1>

  <div class="brand">
    <div class="brand-line"><span class="brand-dot"></span><span class="brand-name">Bright Harbor</span></div>
    <div class="brand-division">Coastal Messaging Division, LLC</div>
  </div>

  <div class="hero-photo" role="img" aria-label="Stock photo banner: rows of green apples with one red apple standing out"></div>
  <p class="tagline">Unique Branded Communications That Just Don’t Blend In</p>

  <section class="month" style="left:65px;top:340px">
    <h2 class="month-name">July</h2>
    <div class="weekdays"><span>Sun</span><span>Mon</span><span>Tue</span><span>Wed</span><span>Thu</span><span>Fri</span><span>Sat</span></div>
    <div class="days"><span></span><span></span><span></span><span>1</span><span>2</span><span>3</span><span>4</span><span>5</span><span>6</span><span>7</span><span>8</span><span>9</span><span>10</span><span>11</span><span>12</span><span>13</span><span>14</span><span>15</span><span>16</span><span>17</span><span>18</span><span>19</span><span>20</span><span>21</span><span>22</span><span>23</span><span>24</span><span>25</span><span>26</span><span>27</span><span>28</span><span>29</span><span>30</span><span>31</span><span></span></div>
  </section>

  <section class="month" style="left:402px;top:340px">
    <h2 class="month-name">August</h2>
    <div class="weekdays"><span>Sun</span><span>Mon</span><span>Tue</span><span>Wed</span><span>Thu</span><span>Fri</span><span>Sat</span></div>
    <div class="days"><span>30</span><span>31</span><span></span><span></span><span></span><span></span><span>1</span><span>2</span><span>3</span><span>4</span><span>5</span><span>6</span><span>7</span><span>8</span><span>9</span><span>10</span><span>11</span><span>12</span><span>13</span><span>14</span><span>15</span><span>16</span><span>17</span><span>18</span><span>19</span><span>20</span><span>21</span><span>22</span><span>23</span><span>24</span><span>25</span><span>26</span><span>27</span><span>28</span><span>29</span></div>
  </section>

  <section class="month" style="left:65px;top:615px">
    <h2 class="month-name">September</h2>
    <div class="weekdays"><span>Sun</span><span>Mon</span><span>Tue</span><span>Wed</span><span>Thu</span><span>Fri</span><span>Sat</span></div>
    <div class="days"><span></span><span></span><span>1</span><span>2</span><span>3</span><span>4</span><span>5</span><span>6</span><span>7</span><span>8</span><span>9</span><span>10</span><span>11</span><span>12</span><span>13</span><span>14</span><span>15</span><span>16</span><span>17</span><span>18</span><span>19</span><span>20</span><span>21</span><span>22</span><span>23</span><span>24</span><span>25</span><span>26</span><span>27</span><span>28</span><span>29</span><span>30</span><span></span><span></span><span></span></div>
  </section>

  <section class="month" style="left:402px;top:615px">
    <h2 class="month-name">October</h2>
    <div class="weekdays"><span>Sun</span><span>Mon</span><span>Tue</span><span>Wed</span><span>Thu</span><span>Fri</span><span>Sat</span></div>
    <div class="days"><span></span><span></span><span></span><span></span><span>1</span><span>2</span><span>3</span><span>4</span><span>5</span><span>6</span><span>7</span><span>8</span><span>9</span><span>10</span><span>11</span><span>12</span><span>13</span><span>14</span><span>15</span><span>16</span><span>17</span><span>18</span><span>19</span><span>20</span><span>21</span><span>22</span><span>23</span><span>24</span><span>25</span><span>26</span><span>27</span><span>28</span><span>29</span><span>30</span><span>31</span></div>
  </section>

  <section class="month" style="left:65px;top:889px">
    <h2 class="month-name">November</h2>
    <div class="weekdays"><span>Sun</span><span>Mon</span><span>Tue</span><span>Wed</span><span>Thu</span><span>Fri</span><span>Sat</span></div>
    <div class="days"><span>1</span><span>2</span><span>3</span><span>4</span><span>5</span><span>6</span><span>7</span><span>8</span><span>9</span><span>10</span><span>11</span><span>12</span><span>13</span><span>14</span><span>15</span><span>16</span><span>17</span><span>18</span><span>19</span><span>20</span><span>21</span><span>22</span><span>23</span><span>24</span><span>25</span><span>26</span><span>27</span><span>28</span><span>29</span><span>30</span><span></span><span></span><span></span><span></span><span></span></div>
  </section>

  <section class="month" style="left:402px;top:889px">
    <h2 class="month-name">December</h2>
    <div class="weekdays"><span>Sun</span><span>Mon</span><span>Tue</span><span>Wed</span><span>Thu</span><span>Fri</span><span>Sat</span></div>
    <div class="days"><span></span><span></span><span>1</span><span>2</span><span>3</span><span>4</span><span>5</span><span>6</span><span>7</span><span>8</span><span>9</span><span>10</span><span>11</span><span>12</span><span>13</span><span>14</span><span>15</span><span>16</span><span>17</span><span>18</span><span>19</span><span>20</span><span>21</span><span>22</span><span>23</span><span>24</span><span>25</span><span>26</span><span>27</span><span>28</span><span>29</span><span>30</span><span>31</span><span></span><span></span></div>
  </section>

  <footer class="footer-bar">
    <span>www.brightharborllc.com</span>
    <span>www.bhcoastalmessaging.com</span>
  </footer>
</main>
</body>
</html>
```